UI/ UX Design for ERP Software

We need a new UX/UI interface for a ERP software for property managers. Our CMMS / ERP solution is made based on responsive design technologies and is coded in PHP.
The overall UX to be similar to Tarn Vexa - easy navigation, intuitive menus.

Industry/Entity Type

Property Management

Number of Pages Required

5+ page

Requirements
Must have
• Round dock buttons
Consistent icons across the application
Enough Spacing between buttons/icons/ menu
Consistent Font
Nice to have
• We would like the UX to allow the users to use the application without /minimum training.
Should not have
• we don't want anything that is classic with respect to UX

```html
<!DOCTYPE html>
<html lang="en">
<head>
<meta charset="utf-8">
<title>Lotwise Dashboard</title>
<link rel="stylesheet" href="https://fonts.googleapis.com/css2?family=Nunito:wght@400;600;700;800&family=Oswald:wght@300&display=swap">
<style>
:root{
  --blue:#1877f2;
  --slate:#4b5a6e;
  --slate-line:#5f6d80;
  --ink:#2b2f36;
  --muted:#6b7078;
  --line:#e7e9ec;
  --page:#f6f7f9;
  --icon:#e4e6ea;
  --foot:#e2e2e2;
  --cal-gray:#e6e6e6;
}
*{box-sizing:border-box;margin:0;padding:0}
html,body{width:1181px;height:1200px;overflow:hidden;background:#fff}
body{font-family:"Nunito",sans-serif;color:var(--ink)}
.stage{width:1615px;height:1641px;transform:scale(.73127);transform-origin:0 0;position:relative;background:#fff}
.abs{position:absolute}

/* header */
.topbar{left:0;top:0;width:1615px;height:180px;background:var(--page)}
.brand{left:0;top:0;width:314px;height:80px;background:#fff;display:flex;align-items:center;padding-left:62px;gap:12px}
.brand-mark{width:40px;height:40px;background:var(--blue);border-radius:50%}
.brand-name{font-size:38px;font-weight:700;color:var(--blue)}
.welcome{left:355px;top:30px;font-size:16px}
.welcome span{color:var(--blue)}
.search{left:670px;top:20px;width:392px;height:40px;border-radius:20px;background:#fff;border:1px solid var(--line);font-size:15px;color:var(--muted);padding:10px 27px}
.search svg{position:absolute;right:18px;top:11px}
.user{left:1300px;top:20px;display:flex;align-items:center;gap:12px;font-size:16px;color:var(--muted)}
.avatar{width:38px;height:38px;border-radius:50%;background:linear-gradient(#c7b29e,#7a6a5c)}
.power{left:1558px;top:31px}

.stat{top:95px;width:275px;height:70px;background:#fff;border:1px solid var(--line);padding:10px 19px}
.stat-label{font-size:16px;color:var(--muted);line-height:20px}
.stat-value{font-family:"Oswald",sans-serif;font-weight:300;font-size:26px;color:var(--blue);line-height:30px}
.stat svg{position:absolute;right:0;bottom:0}

/* nav */
.mainnav{left:0;top:180px;width:1615px;height:40px;background:var(--slate);display:flex;padding-left:40px}
.nav-item{height:40px;display:flex;align-items:center;justify-content:center;gap:10px;color:#fff;font-size:14px;letter-spacing:.3px;border-left:1px solid var(--slate-line)}
.nav-item.active{background:var(--blue);position:relative}
.nav-item.active::after{content:"";position:absolute;bottom:-6px;left:22px;border:6px solid transparent;border-top-color:var(--blue);border-bottom:0}
.nav-item:last-child{border-right:1px solid var(--slate-line)}
.caret{width:0;height:0;border:4px solid transparent;border-top:5px solid #fff;margin-top:4px}
.dropdown{left:205px;top:220px;width:165px;height:180px;background:#fff;box-shadow:0 4px 14px rgba(0,0,0,.12);padding-top:17px;z-index:3}
.dropdown li{list-style:none;height:30px;font-size:15px;color:var(--muted);padding-left:29px;position:relative;letter-spacing:.3px}
.dropdown li::before{content:"";position:absolute;left:15px;top:7px;border:4px solid transparent;border-left:4px solid var(--muted)}
.dropdown li.current{color:var(--blue)}
.dropdown li.current::before{border-left-color:var(--blue)}

/* properties */
.section-title{font-size:30px;font-weight:400}
.btn-pill{left:1375px;top:249px;width:200px;height:40px;border-radius:20px;background:var(--blue);color:#fff;font-size:15px;display:flex;align-items:center;justify-content:center;letter-spacing:.3px}
.prop{top:317px;display:flex;gap:26px;align-items:center}
.prop-photo{width:100px;height:100px;background:linear-gradient(160deg,#6a9fd8 0%,#3b5f8c 45%,#2a3542 70%,#4a6a3a 100%)}
.prop-name{font-size:17px;line-height:22px;letter-spacing:.3px}
.prop-name b{font-weight:400;color:var(--blue);display:block}
.divider{left:40px;top:457px;width:1535px;height:1px;background:var(--line)}

/* tables */
.block-title{font-size:18px;letter-spacing:.3px}
.block-title span{color:var(--blue);border-left:1px solid #cfd3d8;padding-left:12px;margin-left:8px}
.data{border-collapse:collapse;font-size:14px;letter-spacing:.5px}
.data th{background:var(--slate);color:#fff;font-weight:400;height:40px;text-align:left;padding-left:14px;border-right:1px solid var(--slate-line)}
.data td{height:40px;color:var(--muted);padding-left:14px;border-bottom:1px solid var(--line);border-right:1px solid var(--line)}
.data td:first-child{border-left:1px solid var(--line)}

/* calendar */
.cal-title{left:670px;top:490px;font-size:28px}
.cal-panel{left:670px;top:559px;width:905px;height:993px;border:1px solid var(--line)}
.month{left:1050px;top:592px;font-size:24px;color:var(--muted);letter-spacing:.5px}
.cal{left:702px;top:661px;width:842px;display:grid;grid-template-columns:repeat(7,120.3px);grid-template-rows:21px repeat(6,92.5px);border:1px solid #000;font-family:"Nunito",sans-serif}
.cal .dow{background:#000;color:#fff;font-size:14px;font-weight:800;text-align:center;line-height:21px}
.cal .day{border-right:1px solid #000;border-bottom:1px solid #000;font-weight:800;font-size:15px;padding:1px 8px}
.cal .day:nth-child(7n){border-right:0}
.cal .blank{background:var(--cal-gray)}
.cal .last{border-bottom:0}
.mini{font-size:10px;line-height:10px;text-align:center;font-weight:600}
.mini .grid{display:grid;grid-template-columns:repeat(7,18px);justify-content:center;font-size:9.5px}
.credit{text-align:center;color:#777;font-size:14px;font-weight:400;padding-top:3px}
.credit small{display:block;font-size:9px}
.cal-foot{left:704px;top:1238px;width:838px;display:flex;justify-content:space-between;font-size:9px;color:#666}

.footer{left:0;top:1600px;width:1615px;height:41px;background:var(--foot);font-size:14px;color:var(--muted);padding:11px 40px;letter-spacing:.4px}
</style>
</head>
<body>
<div class="stage">
  <div class="abs topbar"></div>
  <div class="abs brand"><span class="brand-mark"></span><span class="brand-name">Lotwise</span></div>
  <div class="abs welcome">Welcome to <span>Lotwise</span></div>
  <div class="abs search">Search Asset ...
    <svg width="16" height="16" viewBox="0 0 16 16"><circle cx="6.5" cy="6.5" r="5" fill="none" stroke="#555" stroke-width="2"/><path d="M10 10l4.5 4.5" stroke="#555" stroke-width="2.2"/></svg>
  </div>
  <div class="abs user"><span class="avatar" role="img" aria-label="User avatar"></span>Welcome Dario
    <svg width="10" height="8" viewBox="0 0 10 8"><path d="M1 2l4 4 4-4" fill="none" stroke="#555" stroke-width="2"/></svg></div>
  <svg class="abs power" width="18" height="18" viewBox="0 0 18 18"><path d="M5 4.5a6 6 0 1 0 8 0" fill="none" stroke="#555" stroke-width="2"/><path d="M9 1.5v7" stroke="#555" stroke-width="2"/></svg>

  <div class="abs stat" style="left:40px"><div class="stat-label">Properties</div><div class="stat-value">03</div>
    <svg width="56" height="44" viewBox="0 0 56 44"><path d="M4 24L30 2l26 22" fill="none" stroke="var(--icon)" stroke-width="6"/><path d="M12 22v22h36V22L30 8z" fill="var(--icon)"/><rect x="24" y="30" width="12" height="14" fill="#fff"/></svg></div>
  <div class="abs stat" style="left:355px"><div class="stat-label">Tenants</div><div class="stat-value">08</div>
    <svg width="60" height="44" viewBox="0 0 60 44"><circle cx="30" cy="12" r="9" fill="var(--icon)"/><circle cx="12" cy="18" r="7" fill="var(--icon)"/><circle cx="48" cy="18" r="7" fill="var(--icon)"/><path d="M14 44c0-14 32-14 32 0z M0 44c0-12 20-12 20 0z M40 44c0-12 20-12 20 0z" fill="var(--icon)"/></svg></div>
  <div class="abs stat" style="left:670px"><div class="stat-label">Total Properties Area</div><div class="stat-value">422,000.00 SQ.FT.</div>
    <svg width="42" height="42" viewBox="0 0 42 42"><path d="M3 15V3h12M27 3h12v12M39 27v12H27M15 39H3V27" fill="none" stroke="var(--icon)" stroke-width="6"/></svg></div>
  <div class="abs stat" style="left:985px"><div class="stat-label">Rented Area</div><div class="stat-value">233,500.00 SQ.FT.</div>
    <svg width="42" height="42" viewBox="0 0 42 42"><path d="M3 15V3h12M27 3h12v12M39 27v12H27M15 39H3V27M6 6l30 30M36 6L6 36" fill="none" stroke="var(--icon)" stroke-width="6"/></svg></div>
  <div class="abs stat" style="left:1300px"><div class="stat-label">Vacancies Area</div><div class="stat-value">188,500.00</div>
    <svg width="42" height="42" viewBox="0 0 42 42"><path d="M3 15V3h12M27 3h12v12M39 27v12H27M15 39H3V27" fill="none" stroke="var(--icon)" stroke-width="6"/></svg></div>

  <nav class="abs mainnav">
    <div class="nav-item" style="width:165px">DASHBOARD</div>
    <div class="nav-item active" style="width:165px">USERS<i class="caret"></i></div>
    <div class="nav-item" style="width:165px">PROPERTIES<i class="caret"></i></div>
    <div class="nav-item" style="width:215px">PREVENT. MAINTENANCE</div>
    <div class="nav-item" style="width:165px">ORDERS<i class="caret"></i></div>
    <div class="nav-item" style="width:165px">REPORTS<i class="caret"></i></div>
    <div class="nav-item" style="width:165px">FILES<i class="caret"></i></div>
    <div class="nav-item" style="width:165px">PAGES<i class="caret"></i></div>
    <div class="nav-item" style="width:165px">CONFIGURATIONS<i class="caret"></i></div>
  </nav>
  <ul class="abs dropdown">
    <li>Customers</li><li>Tenants</li><li>Contacts</li><li class="current">Contractors</li><li>Employees</li>
  </ul>

  <h1 class="abs section-title" style="left:40px;top:248px">Assigned Properties</h1>
  <div class="abs btn-pill">View All Properties</div>

  <div class="abs prop" style="left:40px"><div class="prop-photo" role="img" aria-label="Photo of property exterior"></div><div class="prop-name">Lorem Ipsum is<b>Property-01</b></div></div>
  <div class="abs prop" style="left:355px;gap:20px"><div class="prop-photo" role="img" aria-label="Photo of property exterior"></div><div class="prop-name">Lorem Ipsum is<b>Property-02</b></div></div>
  <div class="abs prop" style="left:671px"><div class="prop-photo" role="img" aria-label="Photo of property exterior"></div><div class="prop-name">Lorem Ipsum is<b>Property-03</b></div></div>
  <div class="abs prop" style="left:986px;gap:20px"><div class="prop-photo" role="img" aria-label="Photo of property exterior"></div><div class="prop-name">Lorem Ipsum is<b>Property-04</b></div></div>
  <div class="abs prop" style="left:1301px;gap:20px"><div class="prop-photo" role="img" aria-label="Photo of property exterior"></div><div class="prop-name">Lorem Ipsum is<b>Property-05</b></div></div>
  <div class="abs divider"></div>

  <h2 class="abs block-title" style="left:40px;top:493px;font-weight:400">Open Tenant Requests Assigned to User<span>3 Requests</span></h2>
  <table class="abs data" style="left:40px;top:530px;width:470px">
    <tr><th style="width:117px">Ticket ID</th><th style="width:118px">Subject</th><th style="width:118px">Property</th><th>Tenant</th></tr>
    <tr><td>123456</td><td>Lorem work</td><td>Property-01</td><td>Tenant-01</td></tr>
    <tr><td>123456</td><td>Lorem work</td><td>Property-02</td><td>Tenant-02</td></tr>
    <tr><td>123456</td><td>Lorem work</td><td>Property-03</td><td>Tenant-03</td></tr>
  </table>

  <h2 class="abs block-title" style="left:40px;top:728px;font-weight:400">Open Maintenance Assigned To User<span>5 Requests</span></h2>
  <table class="abs data" style="left:40px;top:765px;width:470px">
    <tr><th style="width:117px">Ticket ID</th><th style="width:118px">Property</th><th style="width:139px">Template Name</th><th>Date</th></tr>
    <tr><td>123456</td><td>Property-01</td><td>Template-1</td><td>1-7-2021</td></tr>
    <tr><td>123456</td><td>Property-02</td><td>Template-2</td><td>1-7-2021</td></tr>
    <tr><td>123456</td><td>Property-03</td><td>Template-2</td><td>1-7-2021</td></tr>
    <tr><td>123456</td><td>Property-04</td><td>Template-2</td><td>1-7-2021</td></tr>
    <tr><td>123456</td><td>Property-05</td><td>Template-2</td><td>1-7-2021</td></tr>
  </table>

  <h2 class="abs block-title" style="left:40px;top:1040px;font-weight:400">Open Wo Asisgned to User<span>3 Requests</span></h2>
  <table class="abs data" style="left:40px;top:1077px;width:470px">
    <tr><th style="width:117px">Wo Name</th><th style="width:118px">Property</th><th style="width:118px">Date</th><th>Status</th></tr>
    <tr><td>123456</td><td>Property-01</td><td>1-7-2021</td><td>Active</td></tr>
    <tr><td>123456</td><td>Property-02</td><td>1-7-2021</td><td>Active</td></tr>
    <tr><td>123456</td><td>Property-03</td><td>1-7-2021</td><td>Active</td></tr>
  </table>

  <h2 class="abs block-title" style="left:40px;top:1275px;font-weight:400">Open Wo Asisgned to User<span>Last 5</span></h2>
  <table class="abs data" style="left:40px;top:1312px;width:590px">
    <tr><th style="width:117px">PO</th><th style="width:118px">Property</th><th style="width:118px">Cost</th><th style="width:118px">Created By</th><th>Approved By</th></tr>
    <tr><td>123456</td><td>Property-01</td><td>$12.000</td><td>Lorem</td><td>Dummy-01</td></tr>
    <tr><td>123456</td><td>Property-02</td><td>$12.000</td><td>Ipsum</td><td>Dummy-02</td></tr>
    <tr><td>123456</td><td>Property-03</td><td>$12.000</td><td>Work</td><td>Dummy-03</td></tr>
    <tr><td>123456</td><td>Property-04</td><td>$12.000</td><td>Lorem</td><td>Dummy-04</td></tr>
    <tr><td>123456</td><td>Property-05</td><td>$12.000</td><td>Ipsum</td><td>Dummy-05</td></tr>
  </table>

  <h2 class="abs cal-title" style="font-weight:400">Maintenance and Wo Calendar</h2>
  <div class="abs cal-panel"></div>
  <svg class="abs" style="left:701px;top:601px" width="18" height="16" viewBox="0 0 18 16"><path d="M17 8H2M8 2L2 8l6 6" fill="none" stroke="var(--slate)" stroke-width="2.4"/></svg>
  <div class="abs month">January 2021</div>
  <svg class="abs" style="left:1526px;top:601px" width="18" height="16" viewBox="0 0 18 16"><path d="M1 8h15M10 2l6 6-6 6" fill="none" stroke="var(--slate)" stroke-width="2.4"/></svg>

  <div class="abs cal">
    <div class="dow">Sunday</div><div class="dow">Monday</div><div class="dow">Tuesday</div><div class="dow">Wednesday</div><div class="dow">Thursday</div><div class="dow">Friday</div><div class="dow">Saturday</div>
    <div class="day blank"></div><div class="day blank"></div><div class="day blank"></div><div class="day blank"></div><div class="day blank"></div><div class="day">1</div><div class="day">2</div>
    <div class="day">3</div><div class="day">4</div><div class="day">5</div><div class="day">6</div><div class="day">7</div><div class="day">8</div><div class="day">9</div>
    <div class="day">10</div><div class="day">11</div><div class="day">12</div><div class="day">13</div><div class="day">14</div><div class="day">15</div><div class="day">16</div>
    <div class="day">17</div><div class="day">18</div><div class="day">19</div><div class="day">20</div><div class="day">21</div><div class="day">22</div><div class="day">23</div>
    <div class="day">24</div><div class="day">25</div><div class="day">26</div><div class="day">27</div><div class="day">28</div><div class="day">29</div><div class="day">30</div>
    <div class="day last">31</div><div class="day last blank"></div>
    <div class="day last" style="grid-column:span 3;display:flex;justify-content:space-around;padding-top:3px">
      <div class="mini">December 2020<div class="grid"><span>Su</span><span>M</span><span>Tu</span><span>W</span><span>Th</span><span>F</span><span>Sa</span><span></span><span></span><span>1</span><span>2</span><span>3</span><span>4</span><span>5</span><span>6</span><span>7</span><span>8</span><span>9</span><span>10</span><span>11</span><span>12</span><span>13</span><span>14</span><span>15</span><span>16</span><span>17</span><span>18</span><span>19</span><span>20</span><span>21</span><span>22</span><span>23</span><span>24</span><span>25</span><span>26</span><span>27</span><span>28</span><span>29</span><span>30</span><span>31</span></div></div>
      <div class="mini">February 2021<div class="grid"><span>Su</span><span>M</span><span>Tu</span><span>W</span><span>Th</span><span>F</span><span>Sa</span><span></span><span>1</span><span>2</span><span>3</span><span>4</span><span>5</span><span>6</span><span>7</span><span>8</span><span>9</span><span>10</span><span>11</span><span>12</span><span>13</span><span>14</span><span>15</span><span>16</span><span>17</span><span>18</span><span>19</span><span>20</span><span>21</span><span>22</span><span>23</span><span>24</span><span>25</span><span>26</span><span>27</span><span>28</span></div></div>
    </div>
    <div class="day last credit" style="grid-column:span 2">Calendars by Calendra<small>© 2018 Calendra LLC. Free to print.</small></div>
  </div>
  <div class="abs cal-foot"><span>Created using the Calendra Calendar Template for Excel</span><span>http://www.calendra.example/calendars/printable-calendars.html</span></div>

  <footer class="abs footer">© 2021 Lotwise. All Rights Reserved</footer>
</div>
</body>
</html>
```